Web Design needed for logo design project

I am needing an interactive website for TC. Tandem Care Management is a nationwide company that combines the front desk administrative operation within Professional offices (Dental, Chiropractic, Optometry). I am needing a website designed that will provide information for potential new clients that are interested in joining our company to provide to them administrative support. I need a design for the marketing material within the folder, I will add content later. I am looking for clean crisp professional. No dancing teeth, hearts, or EKG signals please. We need it to appeal to 27-40 years old professionals. The professions are equally divided at 50/50 female to male. I already have a logo, it will be attached.
Updates

Target Market(s)

We need it to appeal to 27-40 years old professionals. The professions are equally divided at 50/50 female to male. I already have a logo, it will be attached.

Industry/Entity Type

Marketing

Requirements
Must have
• Needs to be in Word Press. It must have scalability to various screen sizes (Monitor, Phone screen, IPad, etc). Must have a customer portal capability, so professionals can access their information through a portal on the website. Have the capability to run a practice calculator or view a video requiring that it captures the visitors information so I can contact them regarding their interest in the site. Needs to have links to social media.

```html
<!DOCTYPE html>
<html lang="en">
<head>
<meta charset="utf-8">
<title>Tandem Care Management</title>
<link href="https://fonts.googleapis.com/css2?family=PT+Sans:wght@400;700&display=swap" rel="stylesheet">
<style>
  :root {
    --page-bg: #f8f9f9;
    --panel-bg: #e9ebed;
    --panel-edge: #cdd1d5;
    --divider: #c9ced2;
    --brand-dark: #1d4a7c;
    --brand-light: #3aaedc;
    --nav-text: #8e969c;
    --body-text: #9ba4ab;
    --footer-text: #6f777d;
    --icon-grey: #8e969c;
  }
  * { margin: 0; padding: 0; box-sizing: border-box; }
  html, body {
    width: 1200px; height: 1061px; overflow: hidden;
    background: var(--page-bg);
    font-family: "PT Sans", Arial, sans-serif;
  }
  .site { position: relative; width: 1200px; height: 1061px; }

  .site-header {
    position: absolute; left: 180px; top: 72px; width: 850px; height: 97px;
    background: var(--panel-bg); border-bottom: 4px solid var(--panel-edge);
    border-radius: 4px;
  }
  .brand-mark {
    position: absolute; left: 36px; top: 26px;
    font-weight: 700; font-size: 44px; line-height: 44px; letter-spacing: -2px;
    color: var(--brand-dark);
  }
  .main-nav { position: absolute; right: 0; top: 0; height: 93px; display: flex; }
  .main-nav a {
    display: flex; align-items: center; height: 93px; padding: 0 24px;
    font-size: 21px; color: var(--nav-text); text-decoration: none;
    border-left: 1px solid var(--divider);
  }
  .main-nav a:first-child { border-left: none; }
  .main-nav a:last-child { padding-right: 32px; }

  .hero {
    position: absolute; left: 180px; top: 204px; width: 850px; height: 320px;
    border-radius: 4px; overflow: hidden;
    border-bottom: 4px solid var(--panel-edge);
  }
  .hero-photo {
    position: absolute; inset: 0;
    background: linear-gradient(100deg, #e7c99a 0%, #cfb38b 28%, #8a8f9a 55%, #c9ccd1 80%, #dcdee2 100%);
  }
  .hero-title {
    position: absolute; left: 0; top: 61px; width: 506px; height: 97px;
    background: rgba(236, 239, 242, 0.85);
    padding: 8px 0 0 36px;
  }
  .hero-title h1 {
    font-weight: 700; font-size: 42px; line-height: 46px; letter-spacing: 1px;
    color: var(--brand-dark); text-transform: uppercase;
  }
  .hero-title p { font-size: 30px; line-height: 34px; color: var(--brand-dark); }
  .hero-cta {
    position: absolute; right: 0; top: 229px; width: 401px; height: 91px;
    background: rgba(236, 239, 242, 0.85);
    display: flex; align-items: center; padding-left: 20px;
    font-size: 25px; color: var(--brand-light); text-decoration: none;
  }
  .hero-cta svg { margin-left: 10px; }

  .info-card {
    position: absolute; top: 562px; height: 344px;
    background: var(--panel-bg); border-bottom: 4px solid var(--panel-edge);
    border-radius: 4px; padding: 20px 0 0 24px;
  }
  .info-card--about { left: 180px; width: 397px; }
  .info-card--contact { left: 629px; width: 401px; }
  .info-card h2 {
    font-weight: 700; font-size: 32px; line-height: 44px; color: var(--brand-light);
    width: 343px; border-bottom: 2px solid var(--divider); padding-bottom: 6px;
  }
  .info-card p {
    margin-top: 8px; width: 345px;
    font-size: 17.5px; line-height: 24.2px; color: var(--body-text);
  }

  .site-footer {
    position: absolute; left: 0; top: 944px; width: 1200px; text-align: center;
    font-size: 18px; color: var(--footer-text);
  }
  .social-links { display: flex; justify-content: center; gap: 8px; margin-top: 10px; }
  .social-links span {
    width: 21px; height: 21px; border-radius: 3px; background: var(--icon-grey);
  }
</style>
</head>
<body>
<div class="site">
  <header class="site-header">
    <div class="brand-mark">TC</div>
    <nav class="main-nav">
      <a href="#">About</a>
      <a href="#">Services</a>
      <a href="#">Contact Us</a>
      <a href="#">Client Login</a>
    </nav>
  </header>

  <section class="hero">
    <div class="hero-photo" role="img" aria-label="Soft-focus photo of an office desk with a receptionist on the phone"></div>
    <div class="hero-title">
      <h1>Tandem Care</h1>
      <p>Office administration, solved.</p>
    </div>
    <a class="hero-cta" href="#">Learn more about our services
      <svg width="16" height="22" viewBox="0 0 16 22"><path d="M3 2 L13 11 L3 20" fill="none" stroke="currentColor" stroke-width="3.5"/></svg>
    </a>
  </section>

  <section class="info-card info-card--about">
    <h2>About Us</h2>
    <p>Tandem Care Management is a nation&shy;wide company that combines the front desk administrative operation within Professional offices (Dental, Chiropractic, Optometry). Tandem Care Management is a nationwide company that combines the front desk administrative operation within Professional offices (Dental, Chiro&shy;practic, Optometry). Tandem Care Man&shy;</p>
  </section>

  <section class="info-card info-card--contact">
    <h2>Get In Touch</h2>
    <p>Tandem Care Management is a nation&shy;wide company that combines the front desk administrative operation within Professional offices (Dental, Chiropractic, Optometry). Tandem Care Management is a nationwide company that combines the front desk administrative operation within Professional offices (Dental, Chiro&shy;practic, Optometry). Tandem Care Man&shy;</p>
  </section>

  <footer class="site-footer">
    <div>&copy; 2014 Tandem Care Management</div>
    <div class="social-links">
      <span aria-label="Social link one"></span>
      <span aria-label="Social link two"></span>
      <span aria-label="Social link three"></span>
    </div>
  </footer>
</div>
</body>
</html>
```